Business card design needed

My company does everything from wiring up your exisiting entertainment system, to installing a complete new system for you. We can mount your plasma on the wall, install an aerial point for you, setup some surround sound in your outdoor area or install a new cinema room in your house. Any Audio or Visual requirements you may have we can provide these for you. If you want to have a party to remember at your place or just some chilled sounds by the pool, we can give you just the right size system.

Industry/Entity Type

Entertainment

Contact Information for Business Card

The Tune Crew
Colin Pemberton
e| colin@thetunecrew.com.au
w| www.thetunecrew.com.au
m| 0412 576 208

Requirements
Must have
• The logo that i have uploaded is just a starter...something similar to this but not exact or any new suggestions you have would be great too. Colour choice we are pretty easy on we did think Red and Yellow but happy to take advice, something that stands out from the rest i guess.

```html
<!DOCTYPE html>
<html lang="en">
<head>
<meta charset="utf-8">
<title>The Tune Crew – Business Cards</title>
<link rel="stylesheet" href="https://fonts.googleapis.com/css2?family=Open+Sans:wght@400;700&display=swap">
<style>
  :root {
    --backdrop: #b5b5b5;
    --card: #ffffff;
    --red: #ec2b33;
    --yellow: #fbf68a;
    --pink: #f7b4b6;
    --cream: #fefbd8;
    --ink: #4a4a4a;
    --ink-soft: #6f6f6f;
  }
  * { box-sizing: border-box; margin: 0; padding: 0; }
  html, body { width: 1200px; height: 1000px; overflow: hidden; }
  body {
    background: var(--backdrop);
    font-family: "Open Sans", Verdana, sans-serif;
    position: relative;
  }
  .card {
    position: absolute;
    left: 270px;
    width: 660px;
    height: 380px;
    background: var(--card);
    overflow: hidden;
  }
  .card--front { top: 80px; }
  .card--back { top: 540px; }

  .brand {
    position: absolute;
    left: 40px;
    top: 40px;
    display: flex;
    align-items: center;
    gap: 10px;
  }
  .brand__square { width: 26px; height: 26px; background: var(--yellow); }
  .brand__name { color: var(--red); font-weight: 700; font-size: 30px; letter-spacing: -0.5px; }

  /* front */
  .front__yellow { position: absolute; left: 345px; top: 95px; width: 175px; height: 285px; background: var(--yellow); }
  .front__red { position: absolute; left: 405px; top: 60px; width: 255px; height: 300px; background: var(--red); }
  .front__wordmark {
    position: absolute; left: 425px; top: 78px;
    color: var(--pink); font-weight: 700; font-size: 66px; line-height: 0.95; letter-spacing: -1px;
  }
  .contact { position: absolute; left: 40px; top: 215px; color: var(--ink-soft); }
  .contact__name { color: var(--ink); font-weight: 700; font-size: 27px; letter-spacing: 1px; margin-bottom: 14px; }
  .contact__line { font-size: 19px; margin-bottom: 10px; }
  .contact__label { color: var(--ink); font-weight: 700; }

  /* back */
  .back__yellow { position: absolute; left: 310px; top: 0; width: 350px; height: 320px; background: var(--yellow); }
  .back__wordmark {
    position: absolute; left: 335px; top: 22px;
    color: var(--cream); font-weight: 700; font-size: 64px; line-height: 0.95; letter-spacing: -1px;
  }
  .back__band {
    position: absolute; left: 30px; top: 245px; width: 598px; height: 135px;
    background: var(--red); display: flex; align-items: center; justify-content: center;
    color: #fff; font-size: 29px;
  }
  .back__band b { margin-right: 8px; }
</style>
</head>
<body>
  <section class="card card--front">
    <div class="front__yellow"></div>
    <div class="front__red"></div>
    <div class="front__wordmark">The<br>Tune<br>Crew</div>
    <div class="brand"><span class="brand__name">The Tune Crew</span><span class="brand__square"></span></div>
    <div class="contact">
      <p class="contact__name">Colin Pemberton</p>
      <p class="contact__line"><span class="contact__label">e|</span> colin@thetunecrew.com.au</p>
      <p class="contact__line"><span class="contact__label">m|</span> 0412 576 208</p>
    </div>
  </section>

  <section class="card card--back">
    <div class="back__yellow"></div>
    <div class="back__wordmark">The<br>Tune Crew</div>
    <div class="brand"><span class="brand__name">The Tune Crew</span><span class="brand__square"></span></div>
    <div class="back__band"><b>w|</b> www.thetunecrew.com.au</div>
  </section>
</body>
</html>
```